TLPB Business Card Design

Business card for sole operator professional civil and traffic engineer.
Clients are developers and planners who require assistance with traffic strategic master planning advice and design development for access and infrastructure associated with the development.
Colours already in use are greens for the business name and black for other legend. The attached file shows the letterhead template which is currently in use.
Target Market(s)
Professional Clients in development industry
Most clients known to the Principal and card is mostly required to allow ongoing contact
Industry/Entity Type
Business
Contact Information for Business Card
DESMOND HALVERTON CONSULTING SERVICES
ABN 37 818 502 194
PO Box 871 KERRAWAY NSW 2619
Desmond Halverton 0431 558 906
desmond.halverton@quillmarsh.net

```html
<!DOCTYPE html>
<html lang="en">
<head>
<meta charset="utf-8">
<title>TLPB Business Card</title>
<link rel="stylesheet" href="https://fonts.googleapis.com/css2?family=Cinzel:wght@500&family=Open+Sans:wght@400;600;700&display=swap">
<style>
  :root {
    --stage: #e9e9e6;
    --green: #2fa84f;
    --green-deep: #1f8a3c;
    --black: #111111;
    --card-dark-top: #1b1b1b;
    --card-dark-bottom: #050505;
    --white: #ffffff;
    --ink: #1a1a1a;
  }
  * { box-sizing: border-box; margin: 0; padding: 0; }
  html, body {
    width: 1200px; height: 784px; overflow: hidden;
    background: var(--stage);
  }
  .canvas {
    position: relative; width: 1200px; height: 784px;
    display: flex; align-items: center; justify-content: center; gap: 40px;
  }
  .card {
    position: relative; width: 540px; height: 309px; overflow: hidden;
    box-shadow: 0 6px 18px rgba(0,0,0,0.18);
  }

  /* Front (dark) */
  .card-front {
    background: radial-gradient(ellipse at 50% 40%, var(--card-dark-top), var(--card-dark-bottom) 75%);
    display: flex; flex-direction: column; align-items: center; justify-content: center;
  }
  .brand-mark {
    font-family: "Open Sans", sans-serif; font-weight: 700;
    color: var(--green); letter-spacing: 4px; line-height: 1;
  }
  .card-front .brand-mark { font-size: 64px; }
  .company-name {
    font-family: "Cinzel", serif; font-weight: 500; color: var(--green);
    white-space: nowrap;
  }
  .card-front .company-name { font-size: 19px; margin-top: 18px; letter-spacing: 0.5px; }

  /* Back (white) */
  .card-back { background: var(--white); }
  .card-back .brand {
    position: absolute; left: 92px; top: 36px;
  }
  .card-back .brand-mark { font-size: 46px; }
  .card-back .company-name {
    font-size: 13px; position: absolute; left: 40px; top: 102px; letter-spacing: 0.3px;
  }
  .person { position: absolute; left: 62px; top: 140px; }
  .person-name {
    font-family: "Open Sans", sans-serif; font-weight: 600; font-size: 17px; color: var(--green-deep);
  }
  .person-role {
    font-family: "Open Sans", sans-serif; font-size: 9.5px; color: var(--ink); margin-top: 1px;
  }
  .contact-list {
    position: absolute; left: 40px; top: 192px; list-style: none;
    font-family: "Open Sans", sans-serif; font-size: 13px; color: var(--ink); line-height: 17px;
  }
  .contact-list li { display: flex; align-items: center; gap: 6px; }
  .contact-list svg { width: 13px; height: 13px; flex: none; fill: var(--green); }
  .contact-list .abn { padding-left: 19px; }
  .footer-band { position: absolute; left: 0; bottom: 0; width: 540px; height: 50px; }
</style>
</head>
<body>
<main class="canvas">

  <section class="card card-front" aria-label="Card front">
    <div class="brand-mark">TLPB</div>
    <div class="company-name">DESMOND HALVERTON CONSULTING SERVICES</div>
  </section>

  <section class="card card-back" aria-label="Card back">
    <div class="brand"><div class="brand-mark">TLPB</div></div>
    <div class="company-name">DESMOND HALVERTON CONSULTING SERVICES</div>

    <div class="person">
      <div class="person-name">Desmond Halverton</div>
      <div class="person-role">Managing Director</div>
    </div>

    <ul class="contact-list">
      <li>
        <svg viewBox="0 0 24 24" aria-hidden="true"><path d="M6.6 10.8a15.1 15.1 0 0 0 6.6 6.6l2.2-2.2c.3-.3.7-.4 1-.2 1.1.4 2.3.6 3.6.6.6 0 1 .4 1 1V20c0 .6-.4 1-1 1C10.6 21 3 13.4 3 4c0-.6.4-1 1-1h3.5c.6 0 1 .4 1 1 0 1.3.2 2.5.6 3.6.1.3 0 .7-.2 1z"/></svg>
        <span>0431 558 906</span>
      </li>
      <li>
        <svg viewBox="0 0 24 24" aria-hidden="true"><path d="M12 3 2 12h3v8h5v-6h4v6h5v-8h3z"/></svg>
        <span>PO Box 871 KERRAWAY NSW 2619</span>
      </li>
      <li>
        <svg viewBox="0 0 24 24" aria-hidden="true"><path d="M3 5h18v14H3zm2 2v.5l7 4.5 7-4.5V7zm0 3v7h14v-7l-7 4.5z"/></svg>
        <span>desmond.halverton@quillmarsh.net</span>
      </li>
      <li class="abn">ABN 37 818 502 194</li>
    </ul>

    <svg class="footer-band" viewBox="0 0 540 50" preserveAspectRatio="none" aria-hidden="true">
      <polygon points="0,38 540,10 540,14 0,42" fill="var(--green)"/>
      <polygon points="0,42 540,14 540,50 0,50" fill="var(--black)"/>
      <rect x="0" y="45" width="540" height="2" fill="var(--green)"/>
    </svg>
  </section>

</main>
</body>
</html>
```